Structural Engineering Company needs ad for magazine

We are an engineering office for structural engineering in the entertainment industry. Our focus are concert stages, festival structures, grand stands and exhibition booths. Our customers are mainly from Europe, we realize the projects worldwide. Typical customers are designer, architects, stage builders, exhibition builder and technical service provider. We are creating structural analyses, technical consulting, technical drawings and risk assessment. We are working on mid size and major events.
Some technical notes:
- CMYK profile needed, minimum 300 dpi for raster graphic
- Our primary color is Petrol. Favourite is petrol, coral and grey (black). Please use palette shown below.
- Our font in documents is Myriad. Regular at 10 pt for text and Light at 16-24pt for titles.
- The format for the ad is 61 x 127 mm (portrait) or 185 x 46 mm (landscape). Which one is up to you.
To the content:
- For contact details we just want to provide our web address "belsokar.de" and/or our e-mail "info@belsokar.de"
- Attached are some Logo files and photos.
- The ad do not advertise a specific product. It is more a general advertisement for the company.
- The language for the ad should be German. Below are keywords in English and corresponding German translation. You do not need to place all Keywords, it is just a brainstorming list to help you. You are also welcome to use other text. We will help with translation, if necessary.
- we like discussing ideas to get better results, so also if you have questions, please ask.
- If you need information that we haven't thought of yet, please ask.
Our slogan (also in Germany): event meets engineering
Service Keywords EN / DE
- Structural Analysis / Statische Berechnungen
- Risk Assessment / Risikobewertungen
- Consulting & Design / Beratung & Konstruktion
Technical Keywords EN / DE
- Stage machinery / Bühnentechnik
- Scaffolding / Gerüstbau
- Exhibition Booths / Messebauten
- Tents / Zelte
- Temporary Structures / Fliegende Bauten
- Truss / Traversen
- Stages / Bühnen
- Grand Stands / Tribünen
- Leightweight Construction / Leichtbau
- Steel Construction / Stahlbau
- Amusement Rides / Fahrgeschäfte
Look and feel
Each slider illustrates characteristics of the customer's brand and the style your logo design should communicate.

```html
<!DOCTYPE html>
<html lang="de">
<head>
<meta charset="utf-8">
<title>Event trifft Technik – Anzeige</title>
<link href="https://fonts.googleapis.com/css2?family=Montserrat:wght@300;400;500;600;700&display=swap" rel="stylesheet">
<style>
  :root{
    --stage:#e0e5e5;
    --teal:#7ff5e3;
    --teal-text:#6fe6da;
    --tick:#4fd4c6;
    --pink:#ff5fb0;
    --ink:#1b1b1b;
    --paper:#ffffff;
  }
  html,body{margin:0;padding:0;width:1200px;height:1200px;overflow:hidden;background:var(--stage);}
  .ad{
    position:absolute;left:120px;top:414px;width:938px;height:233px;
    background:var(--paper);overflow:hidden;font-family:'Montserrat',sans-serif;color:var(--ink);
    box-shadow:0 6px 14px rgba(0,0,0,.25);
  }
  .ad svg.shapes{position:absolute;left:0;top:0;}
  .photo{position:absolute;left:551px;top:0;width:387px;height:233px;
    background:linear-gradient(180deg,#4a5458 0%,#9aa4a8 22%,#3d7fb8 45%,#5fd0cf 58%,#b4b8bc 70%,#dcdcd8 100%);}

  .headline{position:absolute;left:0;top:0;margin:0;}
  .headline span{position:absolute;left:25px;display:block;line-height:1;white-space:nowrap;}
  .headline .event{top:4px;font-size:55px;font-weight:300;color:var(--teal-text);}
  .headline .trifft{top:47px;left:23px;font-size:54px;font-weight:400;color:var(--pink);}
  .headline .technik{top:92px;left:23px;font-size:40px;font-weight:400;color:var(--teal-text);}

  .tech{position:absolute;left:234px;top:18px;}
  .tech h2{margin:0;font-size:14px;line-height:1;font-weight:700;color:var(--pink);}
  .tech h2 em{font-style:normal;color:var(--teal-text);}
  .tech-list{position:absolute;left:0;top:25px;list-style:none;margin:0;padding:0;width:210px;
    display:grid;grid-template-columns:102px 108px;grid-auto-flow:column;grid-template-rows:repeat(5,18px);}
  .tech-list li{display:flex;align-items:center;gap:4px;font-size:8px;font-weight:600;white-space:nowrap;}
  .tech-list svg{width:9px;height:9px;flex:none;}

  .thumb{position:absolute;width:62px;height:47px;border-radius:6px;}
  .thumb.a{left:412px;top:32px;background:linear-gradient(135deg,#5f8a4a,#c9b58c 60%,#8a7a60);}
  .thumb.b{left:477px;top:32px;background:linear-gradient(160deg,#3d3a4a,#b43a6a 55%,#4a2a3a);}
  .thumb.c{left:412px;top:82px;background:linear-gradient(135deg,#2a3fb0,#8a6ae0 50%,#d070c8);}
  .thumb.d{left:477px;top:82px;background:linear-gradient(135deg,#2a1a4a,#6a3ad0 55%,#1a1030);}

  .services-box{
    position:absolute;left:21px;top:134px;width:176px;height:99px;background:var(--pink);
    border-radius:6px 6px 0 0;box-shadow:4px 0 8px rgba(0,0,0,.25);
  }
  .services-box h2{position:absolute;left:12px;top:4px;margin:0;font-size:15px;line-height:1;font-weight:400;color:#2a2a2a;white-space:nowrap;}
  .services-box h2 em{font-style:normal;color:var(--teal);}
  .service-list{list-style:none;margin:0;padding:0;}
  .service-list li{position:absolute;left:16px;display:flex;gap:3px;font-size:8.8px;line-height:10.5px;color:#1d1d1d;white-space:nowrap;}
  .service-list li.calc{top:23px;}
  .service-list li.risk{top:52px;}
  .service-list li.consult{top:69px;}
  .service-list svg{flex:none;width:13px;height:12px;margin-top:-1px;}

  .brand{position:absolute;left:228px;top:0;color:var(--ink);font-weight:500;line-height:1;}
  .brand .name{position:absolute;left:0;top:181px;font-size:15px;letter-spacing:3.4px;white-space:nowrap;}
  .brand .sub{position:absolute;left:0;top:198px;font-size:9.5px;font-weight:400;letter-spacing:2.4px;white-space:nowrap;}

  .contact{position:absolute;left:395px;display:flex;align-items:center;gap:4px;font-size:12px;line-height:1;color:#1d1d1d;white-space:nowrap;}
  .contact .icon{width:20px;height:14px;background:var(--pink);border-radius:4px;display:flex;align-items:center;justify-content:center;}
  .contact.web{top:169px;}
  .contact.mail{top:199px;}
</style>
</head>
<body>
<div class="ad">
  <div class="photo" role="img" aria-label="Foto: Bühnenaufbau in einem Stadion mit Traversentürmen, Kran und Arbeitern"></div>
  <svg class="shapes" width="938" height="233" viewBox="0 0 938 233">
    <path d="M0,0 H551 C556,80 590,170 631,233 H0 Z" fill="var(--paper)"/>
    <path d="M0,154 H540 C580,154 600,180 631,233 H0 Z" fill="var(--teal)"/>
  </svg>

  <h1 class="headline"><span class="event">EVENT</span><span class="trifft">TRIFFT</span><span class="technik">TECHNIK</span></h1>

  <section class="tech">
    <h2>TECHNICAL <em>SERVICES</em></h2>
    <ul class="tech-list">
      <li><svg viewBox="0 0 10 10"><circle cx="5" cy="5" r="4.3" fill="none" stroke="var(--tick)" stroke-width="1"/><path d="M3,5.2 4.4,6.5 7,3.6" fill="none" stroke="var(--tick)" stroke-width="1"/></svg>Bühnentechnik</li>
      <li><svg viewBox="0 0 10 10"><circle cx="5" cy="5" r="4.3" fill="none" stroke="var(--tick)" stroke-width="1"/><path d="M3,5.2 4.4,6.5 7,3.6" fill="none" stroke="var(--tick)" stroke-width="1"/></svg>Gerüstbau</li>
      <li><svg viewBox="0 0 10 10"><circle cx="5" cy="5" r="4.3" fill="none" stroke="var(--tick)" stroke-width="1"/><path d="M3,5.2 4.4,6.5 7,3.6" fill="none" stroke="var(--tick)" stroke-width="1"/></svg>Messebauten</li>
      <li><svg viewBox="0 0 10 10"><circle cx="5" cy="5" r="4.3" fill="none" stroke="var(--tick)" stroke-width="1"/><path d="M3,5.2 4.4,6.5 7,3.6" fill="none" stroke="var(--tick)" stroke-width="1"/></svg>Fahrgeschäfte</li>
      <li><svg viewBox="0 0 10 10"><circle cx="5" cy="5" r="4.3" fill="none" stroke="var(--tick)" stroke-width="1"/><path d="M3,5.2 4.4,6.5 7,3.6" fill="none" stroke="var(--tick)" stroke-width="1"/></svg>Stahlbau</li>
      <li><svg viewBox="0 0 10 10"><circle cx="5" cy="5" r="4.3" fill="none" stroke="var(--tick)" stroke-width="1"/><path d="M3,5.2 4.4,6.5 7,3.6" fill="none" stroke="var(--tick)" stroke-width="1"/></svg>Bühnen</li>
      <li><svg viewBox="0 0 10 10"><circle cx="5" cy="5" r="4.3" fill="none" stroke="var(--tick)" stroke-width="1"/><path d="M3,5.2 4.4,6.5 7,3.6" fill="none" stroke="var(--tick)" stroke-width="1"/></svg>Tribünen</li>
      <li><svg viewBox="0 0 10 10"><circle cx="5" cy="5" r="4.3" fill="none" stroke="var(--tick)" stroke-width="1"/><path d="M3,5.2 4.4,6.5 7,3.6" fill="none" stroke="var(--tick)" stroke-width="1"/></svg>Leichtbau</li>
      <li><svg viewBox="0 0 10 10"><circle cx="5" cy="5" r="4.3" fill="none" stroke="var(--tick)" stroke-width="1"/><path d="M3,5.2 4.4,6.5 7,3.6" fill="none" stroke="var(--tick)" stroke-width="1"/></svg>Traversen</li>
      <li><svg viewBox="0 0 10 10"><circle cx="5" cy="5" r="4.3" fill="none" stroke="var(--tick)" stroke-width="1"/><path d="M3,5.2 4.4,6.5 7,3.6" fill="none" stroke="var(--tick)" stroke-width="1"/></svg>Zelte</li>
    </ul>
  </section>

  <div class="thumb a" role="img" aria-label="Foto: Holzpavillon im Park"></div>
  <div class="thumb b" role="img" aria-label="Foto: Konzertbühne mit Lichtshow"></div>
  <div class="thumb c" role="img" aria-label="Foto: Traversen in blauem Licht"></div>
  <div class="thumb d" role="img" aria-label="Foto: LED-Scheinwerfer in violettem Licht"></div>

  <section class="services-box">
    <h2>OUR <em>SERVICES</em></h2>
    <ul class="service-list">
      <li class="calc"><svg viewBox="0 0 12 12"><rect x="1" y="2" width="8" height="6" fill="#222"/><circle cx="9" cy="8.5" r="2.3" fill="#222"/></svg><span>Statische<br>Berechnungen</span></li>
      <li class="risk"><svg viewBox="0 0 12 12"><rect x="2" y="1" width="7" height="10" fill="#222"/><rect x="4" y="0" width="3" height="2" fill="#222"/></svg><span>Risikobewertungen</span></li>
      <li class="consult"><svg viewBox="0 0 12 12"><circle cx="3" cy="3" r="1.5" fill="#222"/><circle cx="9" cy="3" r="1.5" fill="#222"/><rect x="1.5" y="5" width="3" height="5" fill="#222"/><rect x="7.5" y="5" width="3" height="5" fill="#222"/><rect x="4.5" y="7" width="3" height="1.5" fill="#222"/></svg><span>Beratung &amp;<br>Konstruktion</span></li>
    </ul>
  </section>

  <div class="brand"><span class="name">BELSOKAR</span><span class="sub">ENGINEERING</span></div>

  <div class="contact web"><span class="icon"><svg width="11" height="11" viewBox="0 0 12 12" fill="none" stroke="#222" stroke-width="0.9"><circle cx="6" cy="6" r="5"/><ellipse cx="6" cy="6" rx="2.2" ry="5"/><path d="M1,6H11M2,3.3H10M2,8.7H10"/></svg></span>belsokar.de</div>
  <div class="contact mail"><span class="icon"><svg width="12" height="9" viewBox="0 0 12 9" fill="none" stroke="#222" stroke-width="1"><rect x="0.5" y="0.5" width="11" height="8"/><path d="M0.5,0.5 6,5 11.5,0.5M0.5,8.5 4.5,4M11.5,8.5 7.5,4"/></svg></span>info@belsokar.de</div>
</div>
</body>
</html>
```